Redesign existing website

We would like a redesign of the website http://www.vestacorpinsights.com that creates a more modern, up to date look.

Talvey Research creates software for social science research and is focused on making the software user friendly and easy to use. We would like to convey seriousness, but also
a very up to date, just released look.

Feel free to modify the logo if you wish.

Target Market(s)

Academics, researchers

Industry/Entity Type

Software

Requirements
Must have
• The design should incorporate the same information as the current website.

```html
<!DOCTYPE html>
<html lang="en">
<head>
<meta charset="utf-8">
<title>Talvey Research</title>
<link href="https://fonts.googleapis.com/css2?family=Dosis:wght@400;500&family=PT+Sans:ital,wght@0,400;0,700;1,400&family=Roboto:wght@300&family=Libre+Baskerville&display=swap" rel="stylesheet">
<style>
:root{
  --blue:#1f3f9e;
  --blue-dark:#17307f;
  --orange:#f7b036;
  --orange-light:#fcc85c;
  --text:#555;
  --muted:#8a8a8a;
  --band:#f2f2f2;
  --footer:#333;
  --footer-text:#cfcfcf;
  --white:#fff;
}
*{margin:0;padding:0;box-sizing:border-box}
html,body{width:949px;height:1200px;overflow:hidden;background:var(--white)}
body{position:relative;font-family:"PT Sans",sans-serif;color:var(--text)}
.abs{position:absolute}

/* header */
.brand{left:30px;top:20px;display:flex;flex-direction:column;align-items:center;width:180px}
.brand-mark{width:74px;height:74px;border-radius:50%;background:var(--blue);border:4px solid #d9def0}
.brand-name{margin-top:8px;font-size:22px;color:var(--blue);font-weight:400;letter-spacing:.5px;white-space:nowrap}
.phones{left:482px;top:51px;font-size:15px;color:var(--muted);display:flex;align-items:center;gap:8px}
.phones svg{margin-right:6px}
.login{left:741px;top:44px;width:75px;height:30px;background:var(--blue);color:var(--white);font-family:"Dosis",sans-serif;font-size:13px;display:flex;align-items:center;justify-content:center}
.social-top{left:827px;top:44px;display:flex;gap:4px}
.social-top span{width:27px;height:28px;border-radius:3px;background:#3b5ea8}
.social-top span:first-child{background:#3fb5dc}

.nav-rule{left:0;top:135px;width:949px;height:6px;background:var(--orange)}
.nav{left:329px;top:100px;width:563px;height:41px;background:linear-gradient(var(--orange-light),var(--orange));border-radius:6px 6px 0 0;display:flex;padding-left:12px}
.nav a{font-family:"Dosis",sans-serif;font-size:13px;color:var(--white);text-decoration:none;display:flex;align-items:center;justify-content:center;height:41px;border-right:1px solid rgba(255,255,255,.35)}
.nav a.active{background:var(--blue);margin-top:2px;height:39px;border-right:none}

/* hero */
.hero{left:0;top:141px;width:949px;height:277px;background:radial-gradient(circle at 20% 30%,#3a63c4,#1f3f9e 60%,#17307f);overflow:hidden}
.hero h1{position:absolute;left:31px;top:46px;font-family:"Roboto",sans-serif;font-weight:300;font-size:27px;line-height:32px;color:var(--white)}
.hero-btn{position:absolute;left:33px;top:167px;width:203px;height:40px;border-radius:20px;background:linear-gradient(var(--orange-light),var(--orange));color:var(--white);font-size:19px;display:flex;align-items:center;justify-content:center}
.hero-dots{position:absolute;left:32px;top:251px;display:flex;gap:11px}
.hero-dots span{width:12px;height:12px;border-radius:50%;background:#1a1f33}
.hero-dots span:first-child{background:var(--white)}
.hero-shot{position:absolute;left:396px;top:32px;width:497px;height:245px;border-radius:5px 5px 0 0;background:linear-gradient(#dde8f7,#c4d8f2);border:2px solid #aac0e0}

/* customers */
.customers-title{left:0;top:457px;width:949px;text-align:center;font-family:"Dosis",sans-serif;font-size:11.5px;color:var(--muted);letter-spacing:.3px}
.customers{left:77px;top:485px;width:762px;height:51px;background:#f1f1f1;display:flex;align-items:center;justify-content:space-around}
.customers span{font-weight:700;font-size:19px;color:#666}
.rule{left:31px;top:551px;width:865px;height:1px;background:#ddd}

/* intro */
.intro{left:31px;top:574px;width:594px}
.intro h2{font-family:"Dosis",sans-serif;font-weight:400;font-size:21px;color:#333;margin-bottom:2px}
.intro p{font-size:12.7px;line-height:17.8px;padding-left:1px}
.release{left:652px;top:583px;width:244px;height:153px;background:linear-gradient(var(--orange-light),var(--orange));text-align:center;color:var(--white)}
.release .kicker{margin-top:13px;font-size:13px}
.release .title{margin-top:7px;font-family:"Libre Baskerville",serif;font-size:25px;line-height:27px}
.release .download{margin:8px auto 0;width:204px;height:28px;border-radius:14px;background:var(--blue);font-size:12px;display:flex;align-items:center;justify-content:center}

/* testimonial */
.band{left:0;top:754px;width:922px;height:162px;background:var(--band)}
.band-line{left:31px;width:868px;height:5px;background:#e4e4e4}
.quote{left:33px;top:806px;width:866px;font-style:italic;font-size:15.8px;line-height:23px;color:#a0a0a0}
.quote cite{font-style:normal;color:var(--blue);margin-left:8px}
.quote-dots{left:448px;top:879px;display:flex;gap:4px}
.quote-dots span{width:7px;height:7px;border-radius:50%;background:#ccc}
.quote-dots span:first-child{background:#888}

/* footer */
.footer{left:0;top:945px;width:949px;height:255px;background:var(--footer);color:var(--footer-text)}
.footer h3{position:absolute;top:28px;font-family:"PT Sans",sans-serif;font-weight:400;font-size:13.5px;color:#e8e8e8}
.contact{position:absolute;left:32px;top:71px;font-size:10px;line-height:13px}
.contact p{margin-bottom:13px}
.contact a{color:var(--footer-text);text-decoration:underline}
.newsletter{position:absolute;left:364px;top:68px;width:246px;height:33px;background:#262626;border:1px solid #1c1c1c;display:flex;align-items:center;justify-content:space-between;padding:0 3px 0 11px}
.newsletter .field{font-size:11px;color:#888}
.newsletter .subscribe{width:84px;height:25px;background:linear-gradient(var(--orange-light),var(--orange));color:var(--white);font-size:13px;display:flex;align-items:center;justify-content:center}
.social-foot{position:absolute;left:788px;top:68px;display:flex;gap:11px}
.social-foot span{width:28px;height:28px;border-radius:3px;background:#3b5ea8}
.social-foot span:nth-child(2){background:#3fb5dc}
.social-foot span:nth-child(3){background:#e8732a}
.footer-rule{position:absolute;left:0;top:171px;width:949px;height:1px;background:#444}
.footer-links{position:absolute;left:0;top:185px;width:949px;text-align:center;font-size:10px}
.footer-links a{color:var(--footer-text);text-decoration:none;margin:0 6px}
.copyright{position:absolute;left:0;top:206px;width:949px;text-align:center;font-size:8.5px;color:#8a8a8a}
</style>
</head>
<body>

<header>
  <div class="abs brand">
    <div class="brand-mark"></div>
    <div class="brand-name">Talvey Research</div>
  </div>
  <div class="abs phones">
    <svg width="15" height="11" viewBox="0 0 15 11"><path d="M1 3 Q7.5 -1 14 3 L12 5 L10 4 L10 2.5 Q7.5 1.8 5 2.5 L5 4 L3 5 Z M3.5 6 H11.5 L13 10.5 H2 Z" fill="#555"/></svg>
    <span>612-555-0148</span><span>|</span><span>1-800-555-0172</span>
  </div>
  <div class="abs login">LOGIN</div>
  <div class="abs social-top"><span></span><span></span></div>

  <div class="abs nav-rule"></div>
  <nav class="abs nav">
    <a class="active" style="width:61px">HOME</a>
    <a style="width:140px">PRODUCTS</a>
    <a style="width:114px">ABOUT US</a>
    <a style="width:90px">NEWS</a>
    <a style="width:131px;border-right:none">CONTACT US</a>
  </nav>
</header>

<section class="abs hero">
  <h1>Increasing the Power and<br>Efficiency of Empirical<br>Social Science Research</h1>
  <div class="hero-btn">View Product</div>
  <div class="hero-dots"><span></span><span></span><span></span><span></span></div>
  <div class="hero-shot" role="img" aria-label="Screenshot of the Talvey Data Manager application window"></div>
</section>

<div class="abs customers-title">JUST SOME OF OUR CUSTOMERS</div>
<div class="abs customers">
  <span>Meridel</span><span>Quorvix</span><span>Kelvard</span><span>NRX</span><span>Pellham</span><span>Sundara</span>
</div>
<div class="abs rule"></div>

<section class="abs intro">
  <h2>EMPOWERING THE SOCIAL SCIENCE RESEARCHER</h2>
  <p>Lorem Ipsum is simply dummy text of the printing and typesetting industry. Lorem Ipsum has been the industry's standard dummy text ever since the 1500s, when an unknown printer took a galley of type and scrambled it to make a type specimen book. It has survived not only five centuries, but also the leap into electronic typesetting, remaining essentially unchanged. It was popularised in the 1960s with the release of Typewell sheets containing Lorem Ipsum passages, and more recently with desktop publishing software like Brisco PageSetter including versions of Lorem Ipsum. It is a long established fact that a reader will be distracted by the readable content of a page when looking at its layout. The point of using Lorem Ipsum is that it has a more-or-less normal distribution of letters, as opposed to using 'Content here,</p>
</section>

<aside class="abs release">
  <div class="kicker">Preview Release Available!</div>
  <div class="title">TALVEY DATA<br>MANAGER</div>
  <div class="download">Download Preview Release</div>
</aside>

<section>
  <div class="abs band"></div>
  <div class="abs band-line" style="top:777px"></div>
  <div class="abs band-line" style="top:905px"></div>
  <blockquote class="abs quote">“Lorem Ipsum is simply dummy text of the printing and typesetting industry. Lorem Ipsum has been the industry's standard dummy text ever since the 1500s, when an unknown printer took a galley of”. <cite>— Ledgerline</cite></blockquote>
  <div class="abs quote-dots"><span></span><span></span><span></span></div>
</section>

<footer class="abs footer">
  <h3 style="left:32px">Contact Us</h3>
  <h3 style="left:366px">Sign up for Our Newsletter</h3>
  <h3 style="left:688px">Stay updated on our Social Network</h3>
  <div class="contact">
    <p>Talvey Research, Inc. 2180 Alder Crest Ave<br>Linwood, MD 20817 USA</p>
    <p>(415) 555-0193</p>
    <p><a>info@talveyresearch.com</a></p>
  </div>
  <div class="newsletter"><span class="field">enter your email address</span><span class="subscribe">Subscribe</span></div>
  <div class="social-foot"><span></span><span></span><span></span></div>
  <div class="footer-rule"></div>
  <div class="footer-links"><a>home</a><a>products</a><a>news</a><a>about us</a><a>contact us</a></div>
  <div class="copyright">© Copyright 2011 Talvey Research. All Rights Reserved. &nbsp;Terms &amp; Conditions &nbsp;| &nbsp;&nbsp;Privacy Policy</div>
</footer>

</body>
</html>
```